Poster-style graphics needed for "rock star" Storytelling Coach

Thanks for your interest in my project. I need the FRONT COVER and BACK COVER for our 2018-9 Strategic Storytelling Programs brochure.

I run skills development events for Meridian 300s like Varnholt Bank, Quembo, KorvathWerke, Pravix, Lumiq, etc. The idea is to have first impression of "wow" design and impact that this is SOMETHING DIFFERENT from the usual corporate blah blah blah stuff.

Your inspiration will be from exciting movie posters featuring 5-star reviews ... ( I include a few examples as reference)

This brief is only for Front and Back Cover. (Don't worry about inside - we will use existing program brochure outlines for this). Have fun!

Output: A4 Portrait (VERTICAL) format, colour, PDF and jpeg.

Oh, the really good news is this: whoever wins this, will also get to work on the cover designs for my other company's programs too.

Target Market(s)

Meridian 300 corporates in Asia Pacific - might be HR or CEO or Marketing Department reading it. But it must be "exciting" not "corporate boring square and grey"

Industry/Entity Type

Training

Font styles to use
Sans Serif

Colors
fbed22
f78f20
ec1f27
33a6d7

Requirements
Must have
• FRONT COVER:
• 1.Ned Parrish pic on front cover - front and centre.
• 2. Must look like a 'movie poster' with 5 star reviews, Make it appear important, credible, exciting - make them want to read and share the brochure.
• 3. Reviews (as supplied below) big and bold on the front.
• 4. Headline: Hi, I'm Ned Parrish. "The Perfect Storyteller!" - The Harbinger, UK.
• Subhead: Strategic Storytelling & Presentation Literacy Skills Events 2018-9.
• 4. OWLFENHARE logo. www.owlfenhare-example.com
• --
• BACK COVER:
• 1. Maybe a montage of shots (as provided) to show workshops and activities.
• 2. OWLFENHARE logo
• 3. Call to action:
• Imagine what we could do for you! To unleash your team's strategic storytelling power, contact OWLFENHARE today:
• headowl@owlfenhare-example.com
• Asia/Pacific Storyline +66-81-537-2094.
• Heart Office: 5F Ming Tak House, 42 Ravelin Street, Tai Hang, Hong Kong.
• www.owlfenhare-example.com
• See more stories and clips at youtube: fablewick47
• facebook.com/OWLFENHARE
• --
• Reviews for front page: (use as many as you can/like ... the last ones are the least important ones)
• “You rock! The tips you shared will help me immensely in creating more potent and engaging content.” Producer/Anchor, Orbis Selatan TV, Malaysia.
• “Great! Best course I have taken so far. Ned is an expert in his field. 10/10!” Dr KMR, Director, Brenloch, China.
• “You have transformed the team in a day!” Director O&D, Asia Pacific, Dunmore Haverly.
• “Fantastic! Inspiring, fun, practical – That’s his magic dust. Some of the best training in my 25-year career. ” Managing Director, VERAM.
• “Very inspiring and engaging teacher with highly positive energy. I learned a lot!” Regional Marketing Manager, Pingvale, Singapore.
• “Wonderful. Your energy and professional coaching are so impressive. The skills you taught are very helpful.” Lead R&D Engineer, TK, China.
• “Yeah! Yeah! Yeah! You’re the man, Ned. You helped me a lot in making my talk tighter … really appreciated!” Owen Brasket, Frozen Harbour (Halcyon Prize-winning program airing in 200 countries), Wayfarer Network.
• “Thank you, Ned, for being such an amazing coach. The best of the best – I actually look forward to presentations now. !” Regional Financial Manager, APMEA, BQX Voyages.
• "Ned is truly a subject matter expert." Marketing Executive, Varnholt Bank, Singapore.

```html
<!DOCTYPE html>
<html lang="en">
<head>
<meta charset="utf-8">
<title>OWLFENHARE Storytelling Brochure Covers</title>
<link href="https://fonts.googleapis.com/css2?family=Anton&family=Oswald:wght@300;400;500;600;700&family=Montserrat:wght@300;400&display=swap" rel="stylesheet">
<style>
  :root {
    --bg: #e9e9e9;
    --page: #000000;
    --white: #ffffff;
    --grey-text: #c9c9c9;
    --band: #2b2b2b;
    --star: #f78f20;
    --yellow: #fbed22;
    --red: #ec1f27;
    --blue: #33a6d7;
  }
  * { box-sizing: border-box; margin: 0; padding: 0; }
  html, body { width: 1200px; height: 1200px; overflow: hidden; background: var(--bg); }
  .canvas { position: relative; width: 1200px; height: 1200px; }

  .page {
    position: absolute; top: 340px; width: 489px; height: 692px;
    background: var(--page); overflow: hidden; color: var(--white);
  }
  .page--front { left: 63px; }
  .page--back { left: 630px; }

  /* front cover */
  .stage-light {
    position: absolute; left: 0; top: 0; width: 489px; height: 440px;
    background:
      radial-gradient(ellipse 190px 260px at 250px 70px, rgba(90,110,220,.85), rgba(40,50,140,.45) 55%, rgba(0,0,0,0) 100%),
      linear-gradient(#0d1030, #000 95%);
  }
  .coach-photo {
    position: absolute; left: 74px; top: 130px; width: 266px; height: 300px;
    border-radius: 120px 130px 20px 40px;
    background:
      radial-gradient(ellipse 52px 62px at 148px 60px, #b08366, #7a5442 70%, rgba(60,40,30,0) 100%),
      radial-gradient(ellipse 150px 170px at 150px 230px, #2a2624, #141211 75%, rgba(0,0,0,0) 100%),
      linear-gradient(180deg, rgba(60,50,45,.0) 0%, rgba(30,26,24,.9) 40%, rgba(0,0,0,0) 100%);
  }
  .review { position: absolute; font-family: 'Oswald', sans-serif; color: var(--white); }
  .review__quote { font-weight: 500; font-size: 10.2px; line-height: 1.22; letter-spacing: -.2px; }
  .review__stars { display: flex; gap: 3px; margin: 5px 0 5px; }
  .review__stars svg { width: 12px; height: 12px; }
  .review__source { font-weight: 300; font-size: 8.6px; line-height: 1.25; color: var(--grey-text); letter-spacing: -.2px; }

  .intro {
    position: absolute; left: 0; width: 489px; top: 406px; text-align: center;
    font-family: 'Montserrat', sans-serif; font-weight: 300; font-size: 14px; letter-spacing: .5px;
  }
  .headline { position: absolute; left: 0; top: 420px; width: 489px; height: 110px; }
  .headline__top { font-family: 'Oswald', sans-serif; font-weight: 500; font-size: 40px; fill: var(--white); }
  .headline__main { font-family: 'Anton', sans-serif; font-size: 58px; }
  .attribution {
    position: absolute; left: 0; width: 489px; top: 532px; text-align: center;
    font-family: 'Montserrat', sans-serif; font-weight: 300; font-size: 14px;
  }
  .subhead-band {
    position: absolute; left: 0; top: 571px; width: 489px; height: 31px; background: var(--band);
    display: flex; align-items: center; justify-content: center;
    font-family: 'Oswald', sans-serif; font-weight: 600; font-size: 14.5px; letter-spacing: -.3px;
  }

  .brand {
    position: absolute; width: 178px; height: 56px;
    display: flex; flex-direction: column; align-items: center; justify-content: center; gap: 4px;
  }
  .brand__name { font-family: 'Oswald', sans-serif; font-weight: 700; font-size: 25px; line-height: 1; color: var(--star); letter-spacing: .5px; }
  .brand__tag { font-family: 'Oswald', sans-serif; font-weight: 400; font-size: 5.2px; color: var(--white); letter-spacing: .2px; }
  .page--front .brand { left: 33px; top: 612px; }
  .front-url {
    position: absolute; left: 224px; top: 632px; white-space: nowrap;
    font-family: 'Montserrat', sans-serif; font-weight: 400; font-size: 11px; letter-spacing: 1.3px;
  }

  /* back cover */
  .event-photo {
    position: absolute; left: 0; top: 0; width: 489px; height: 536px;
    background:
      radial-gradient(ellipse 260px 240px at 400px 300px, #4a3a34, #241d1a 60%, rgba(0,0,0,0) 100%),
      radial-gradient(ellipse 180px 140px at 130px 420px, #4d4a4c, #1b1a1c 80%),
      linear-gradient(#0c0c0e, #1a1a1c);
  }
  .cta-headline { position: absolute; left: 0; top: 0; width: 240px; height: 340px; }
  .cta-headline text {
    font-family: 'Anton', sans-serif; fill: #000; stroke: var(--white); stroke-width: 2.2px;
    paint-order: stroke fill; stroke-linejoin: round;
  }
  .page--back .brand { left: 282px; top: 18px; background: rgba(0,0,0,.85); }
  .cta-band {
    position: absolute; left: 0; top: 536px; width: 489px; height: 30px; background: var(--band);
    display: flex; align-items: center; justify-content: center;
    font-family: 'Oswald', sans-serif; font-weight: 600; font-size: 13.5px; letter-spacing: -.3px;
  }
  .contact {
    position: absolute; left: 0; width: 489px; text-align: center;
    font-family: 'Montserrat', sans-serif; font-weight: 400; font-size: 12.5px; color: var(--white);
    display: flex; justify-content: center; align-items: center; gap: 5px; white-space: nowrap;
  }
  .contact svg { width: 12px; height: 12px; flex: none; }
  .contact--phone { top: 577px; }
  .contact--web { top: 599px; font-size: 12px; }
  .contact--address { top: 622px; font-size: 12px; }
  .contact--social { top: 650px; }
  .social-mark { width: 14px; height: 14px; background: var(--blue); display: inline-block; }
  .divider { width: 1px; height: 14px; background: var(--white); margin: 0 3px; }
</style>
</head>
<body>
<div class="canvas">
  <svg width="0" height="0" style="position:absolute">
    <defs>
      <symbol id="star" viewBox="0 0 24 24"><path d="M12 1.5l3.1 7 7.6.7-5.8 5 1.8 7.5L12 17.8 5.3 21.7l1.8-7.5-5.8-5 7.6-.7z" fill="#f78f20"/></symbol>
      <linearGradient id="chrome" x1="0" y1="0" x2="0" y2="1">
        <stop offset="0" stop-color="#ffffff"/>
        <stop offset=".45" stop-color="#bdbdbd"/>
        <stop offset=".6" stop-color="#e8e8e8"/>
        <stop offset="1" stop-color="#8e8e8e"/>
      </linearGradient>
    </defs>
  </svg>

  <section class="page page--front">
    <div class="stage-light"></div>
    <div class="coach-photo" role="img" aria-label="Photo of Ned Parrish, smiling and gesturing with one hand, in a dark jacket under a blue stage spotlight"></div>

    <div class="review" style="left:22px;top:24px;width:125px">
      <p class="review__quote">Great! Best course I have taken so far. Ned is an expert in his field. 10/10!</p>
      <div class="review__stars"><svg><use href="#star"/></svg><svg><use href="#star"/></svg><svg><use href="#star"/></svg><svg><use href="#star"/></svg><svg><use href="#star"/></svg></div>
      <p class="review__source">Dr KMR, Director, Brenloch, China</p>
    </div>
    <div class="review" style="left:166px;top:24px;width:152px">
      <p class="review__quote">Yeah! Yeah! Yeah! You’re the man, Ned. You helped me a lot in making my talk tighter … really appreciated!</p>
      <div class="review__stars"><svg><use href="#star"/></svg><svg><use href="#star"/></svg><svg><use href="#star"/></svg><svg><use href="#star"/></svg><svg><use href="#star"/></svg></div>
      <p class="review__source">Owen Brasket, Frozen Harbour (Halcyon Prize-winning program airing in 200 countries), Wayfarer Network.</p>
    </div>
    <div class="review" style="left:327px;top:28px;width:148px">
      <p class="review__quote">Fantastic! Inspiring, fun, practical - That’s his magic dust. Some of the best training in my 25-year career.</p>
      <div class="review__stars"><svg><use href="#star"/></svg><svg><use href="#star"/></svg><svg><use href="#star"/></svg><svg><use href="#star"/></svg><svg><use href="#star"/></svg></div>
      <p class="review__source">Managing Director, VERAM</p>
    </div>
    <div class="review" style="left:18px;top:112px;width:125px">
      <p class="review__quote">Very inspiring and engaging teacher with highly positive energy. I learned a lot</p>
      <div class="review__stars"><svg><use href="#star"/></svg><svg><use href="#star"/></svg><svg><use href="#star"/></svg><svg><use href="#star"/></svg><svg><use href="#star"/></svg></div>
      <p class="review__source">Regional Marketing Manager,<br>Pingvale, Singapore.</p>
    </div>
    <div class="review" style="left:309px;top:120px;width:165px">
      <p class="review__quote">Ned is truly a subject matter expert</p>
      <div class="review__stars"><svg><use href="#star"/></svg><svg><use href="#star"/></svg><svg><use href="#star"/></svg><svg><use href="#star"/></svg><svg><use href="#star"/></svg></div>
      <p class="review__source">Marketing Executive, Varnholt Bank,<br>Singapore.</p>
    </div>
    <div class="review" style="left:19px;top:208px;width:160px">
      <p class="review__quote">Wonderful. Your energy and profes-<br>sional coaching are so impressive.<br>The skills you taught are very helpful</p>
      <div class="review__stars"><svg><use href="#star"/></svg><svg><use href="#star"/></svg><svg><use href="#star"/></svg><svg><use href="#star"/></svg><svg><use href="#star"/></svg></div>
      <p class="review__source">Lead R&amp;D Engineer,<br>TK, China.</p>
    </div>
    <div class="review" style="left:330px;top:196px;width:140px">
      <p class="review__quote">You rock! The tips you shared will help me immensely in creating more potent and engaging content.</p>
      <div class="review__stars"><svg><use href="#star"/></svg><svg><use href="#star"/></svg><svg><use href="#star"/></svg><svg><use href="#star"/></svg><svg><use href="#star"/></svg></div>
      <p class="review__source">Producer/Anchor, Orbis Selatan TV, Malaysia.</p>
    </div>
    <div class="review" style="left:19px;top:316px;width:175px">
      <p class="review__quote">You have transformed the team in a day!</p>
      <div class="review__stars"><svg><use href="#star"/></svg><svg><use href="#star"/></svg><svg><use href="#star"/></svg><svg><use href="#star"/></svg><svg><use href="#star"/></svg></div>
      <p class="review__source">Director O&amp;D, Asia Pacific, Dunmore Haverly.</p>
    </div>
    <div class="review" style="left:343px;top:302px;width:132px">
      <p class="review__quote">Thank you, Ned, for being such an amazing coach. The best of the best - I actually look for-ward to presentations now.</p>
      <div class="review__stars"><svg><use href="#star"/></svg><svg><use href="#star"/></svg><svg><use href="#star"/></svg><svg><use href="#star"/></svg><svg><use href="#star"/></svg></div>
      <p class="review__source">Regional Financial Manager, APMEA, BQX Voyages.</p>
    </div>

    <p class="intro">HI, I'M NED PARRISH</p>
    <svg class="headline" viewBox="0 420 489 110" aria-label="The Perfect Storyteller">
      <text class="headline__top" x="133" y="464" textLength="224" lengthAdjust="spacingAndGlyphs">THE PERFECT</text>
      <text class="headline__main" x="62" y="522" textLength="364" lengthAdjust="spacingAndGlyphs" fill="url(#chrome)">STORYTELLER</text>
    </svg>
    <p class="attribution">(The Harbinger, UK.)</p>
    <div class="subhead-band">STRATEGIC STORYTELLING &amp; PRESENTATION LITERACY SKILLS EVENTS 2018-9</div>

    <div class="brand">
      <span class="brand__name">OWLFENHARE</span>
      <span class="brand__tag">STRATEGIC STORYTELLING • PRESENTATION PSYCHOLOGY • PITCH COACHING</span>
    </div>
    <p class="front-url">www.owlfenhare-example.com</p>
  </section>

  <section class="page page--back">
    <div class="event-photo" role="img" aria-label="Photo of a theatre audience giving a standing ovation to speakers on stage"></div>
    <svg class="cta-headline" viewBox="0 0 240 340" aria-label="Imagine what we could do for you!">
      <text x="31" y="58" font-size="48" textLength="181" lengthAdjust="spacingAndGlyphs">IMAGINE</text>
      <text x="31" y="132" font-size="69" textLength="181" lengthAdjust="spacingAndGlyphs">WHAT</text>
      <text x="31" y="178" font-size="41" textLength="181" lengthAdjust="spacingAndGlyphs">WE COULD</text>
      <text x="31" y="234" font-size="54" textLength="181" lengthAdjust="spacingAndGlyphs">DO FOR</text>
      <text x="29" y="320" font-size="87" textLength="185" lengthAdjust="spacingAndGlyphs">YOU!</text>
    </svg>
    <div class="brand">
      <span class="brand__name">OWLFENHARE</span>
      <span class="brand__tag">STRATEGIC STORYTELLING • PRESENTATION PSYCHOLOGY • PITCH COACHING</span>
    </div>
    <div class="cta-band">TO UNLEASH YOUR TEAM'S STRATEGIC STORYTELLING POWER, CONTACT OWLFENHARE TODAY</div>

    <p class="contact contact--phone">Asia/Pacific Storyline +66-81-537-2094.</p>
    <p class="contact contact--web">
      <svg viewBox="0 0 24 24"><rect x="2" y="5" width="20" height="14" fill="none" stroke="#ec1f27" stroke-width="2"/><path d="M2 5l10 8 10-8" fill="none" stroke="#ec1f27" stroke-width="2"/></svg>
      headowl@owlfenhare-example.com&nbsp;
      <svg viewBox="0 0 24 24"><circle cx="12" cy="12" r="9" fill="none" stroke="#ec1f27" stroke-width="2"/><path d="M3 12h18M12 3c4 4 4 14 0 18M12 3c-4 4-4 14 0 18" fill="none" stroke="#ec1f27" stroke-width="1.5"/></svg>
      www.owlfenhare-example.com
    </p>
    <p class="contact contact--address">
      <svg viewBox="0 0 24 24"><path d="M12 2a7 7 0 0 0-7 7c0 5 7 13 7 13s7-8 7-13a7 7 0 0 0-7-7z" fill="#ec1f27"/><circle cx="12" cy="9" r="2.5" fill="#000"/></svg>
      5F Ming Tak House, 42 Ravelin Street, Tai Hang, Hong Kong
    </p>
    <p class="contact contact--social">
      <span class="social-mark"></span>&nbsp;@OWLFENHARE
      <span class="divider"></span>
      <span class="social-mark" style="background:var(--red)"></span>&nbsp;@FABLEWICK47
    </p>
  </section>
</div>
</body>
</html>
```